Brightpath Wellness Partners

Please design a business card that is colorful but at the same time easy to read. We are based out on Miami Florida. We are a small start up healthcare company that has been in operation for 1 year. Our clients are Hospitals, Insurance companies, and Manage Care health companies. We are growing quickly and lead the niche we are in. Please make the card 2 sided on the front will be the typical info. Logo, Company Name, Persons Name, Title, Cell #, Office #, Fax#, email, website. No address. On the back we will list 5 services that we do. For example Care Transitions, Case management, Risk assessment, Utilization Review.
Target Market(s)
CEO's and COO's of hospitals and healthcare companies.
Industry/Entity Type
Healthcare

```html
<!DOCTYPE html>
<html lang="en">
<head>
<meta charset="utf-8">
<title>Brightpath Wellness Partners – Business Card</title>
<link rel="stylesheet" href="https://fonts.googleapis.com/css2?family=Comfortaa:wght@300;700&family=Open+Sans:ital,wght@1,300;1,400&display=swap">
<style>
  :root {
    --ink-deep: #0a2238;
    --back-base: #1a3a4c;
    --front-base: #0e3a5c;
    --glow: #1fa6e0;
    --band: rgba(20, 90, 150, 0.55);
    --band-text: #3fb6f0;
    --text-light: #e8f4fb;
    --text-soft: #4ab8ea;
    --brand-blue: #1f6fb5;
    --brand-green: #1fa24a;
    --brand-yellow: #f3dc1c;
    --brand-red: #e2242b;
    --divider: #050b12;
  }
  * { margin: 0; padding: 0; box-sizing: border-box; }
  html, body { width: 917px; height: 1200px; overflow: hidden; background: var(--divider); }
  .canvas { position: relative; width: 917px; height: 1200px; }

  .card-back {
    position: absolute; left: 0; top: 0; width: 917px; height: 593px;
    background:
      radial-gradient(circle at 430px 250px, rgba(31,166,224,0.45), transparent 260px),
      radial-gradient(circle at 720px 160px, rgba(31,166,224,0.25), transparent 180px),
      radial-gradient(circle at 250px 420px, rgba(31,166,224,0.25), transparent 180px),
      var(--back-base);
    overflow: hidden;
  }
  .brand-mark {
    position: absolute; display: flex; align-items: center; gap: 16px;
    font-family: "Comfortaa", sans-serif; font-weight: 700; color: var(--text-light);
  }
  .card-back .brand-mark { left: 0; right: 0; top: 180px; justify-content: center; font-size: 42px; }
  .brand-dot { border-radius: 50%; background: var(--brand-green); flex: none; }
  .card-back .brand-dot { width: 40px; height: 40px; }

  .service-band {
    position: absolute; left: 0; top: 453px; width: 917px; height: 40px;
    background: var(--band);
    display: flex; align-items: center; justify-content: center;
    font-family: "Comfortaa", sans-serif; font-weight: 300; font-size: 21px;
    color: var(--band-text); letter-spacing: -0.2px; white-space: nowrap;
  }

  .card-front-left {
    position: absolute; left: 0; top: 607px; width: 489px; height: 593px;
    background:
      radial-gradient(circle at 230px 180px, rgba(31,166,224,0.4), transparent 230px),
      radial-gradient(circle at 45px 500px, rgba(31,166,224,0.35), transparent 60px),
      var(--front-base);
    overflow: hidden;
  }
  .card-front-left .brand-mark { left: 50px; top: 140px; font-size: 27px; line-height: 1.25; gap: 12px; }
  .card-front-left .brand-dot { width: 28px; height: 28px; }

  .service-legend { position: absolute; left: 107px; top: 321px; list-style: none; }
  .service-legend li {
    display: flex; align-items: center; height: 37px;
    font-family: "Open Sans", sans-serif; font-style: italic; font-weight: 300;
    font-size: 21px; color: var(--text-light);
  }
  .swatch { width: 20px; height: 21px; margin-right: 37px; flex: none; }
  .swatch.blue { background: var(--brand-blue); }
  .swatch.green { background: var(--brand-green); }
  .swatch.yellow { background: var(--brand-yellow); }
  .swatch.red { background: var(--brand-red); }

  .address {
    position: absolute; left: 71px; top: 472px;
    font-family: "Comfortaa", sans-serif; font-weight: 300; font-size: 19px;
    line-height: 23px; color: var(--text-soft);
  }

  .card-front-right {
    position: absolute; left: 489px; top: 607px; width: 428px; height: 593px;
    background:
      radial-gradient(circle at 170px 170px, rgba(31,166,224,0.45), transparent 220px),
      radial-gradient(circle at 330px 120px, rgba(31,166,224,0.25), transparent 150px),
      var(--front-base);
    overflow: hidden;
  }
  .person-name {
    position: absolute; left: 28px; top: 334px;
    font-family: "Comfortaa", sans-serif; font-weight: 700; font-size: 27px; color: var(--text-light);
  }
  .person-title {
    position: absolute; left: 28px; top: 375px;
    font-family: "Open Sans", sans-serif; font-style: italic; font-size: 23px;
    color: var(--text-soft); text-decoration: underline;
  }
  .contact-list { position: absolute; left: 5px; top: 428px; list-style: none; }
  .contact-list li {
    display: flex; align-items: center; height: 23.5px;
    font-family: "Open Sans", sans-serif; font-style: italic; font-size: 23px;
    color: var(--text-light); white-space: nowrap;
  }
  .contact-list li.link { text-decoration: underline; }
  .contact-icon { width: 18px; height: 18px; margin-right: 6px; flex: none; }
</style>
</head>
<body>
<main class="canvas">

  <section class="card-back" aria-label="Card back">
    <div class="brand-mark"><span class="brand-dot"></span>Brightpath Wellness Partners</div>
    <div class="service-band">Care Transitions - Case management - Risk assessment - Utilization Review</div>
  </section>

  <section class="card-front-left" aria-label="Card front, services side">
    <div class="brand-mark"><span class="brand-dot"></span><span>Brightpath Wellness<br>Partners</span></div>
    <ul class="service-legend">
      <li><span class="swatch blue"></span>something 1</li>
      <li><span class="swatch green"></span>SOMETHING 2</li>
      <li><span class="swatch yellow"></span>Something 3</li>
      <li><span class="swatch red"></span>Something 4</li>
    </ul>
    <p class="address">full adress if needed<br>first line<br>second line</p>
  </section>

  <section class="card-front-right" aria-label="Card front, contact side">
    <h1 class="person-name">Name</h1>
    <p class="person-title">Title</p>
    <ul class="contact-list">
      <li><svg class="contact-icon" viewBox="0 0 18 18"><rect x="5" y="1" width="8" height="16" rx="1.5" fill="none" stroke="#e8f4fb" stroke-width="1.6"/><line x1="7" y1="14" x2="11" y2="14" stroke="#e8f4fb" stroke-width="1.4"/></svg>+1 111 111 111</li>
      <li><svg class="contact-icon" viewBox="0 0 18 18"><path d="M4 2 L7 2 L8 6 L6 7.5 Q8 11 10.5 12 L12 10 L16 11 L16 14 Q15 16 12 15.5 Q4 13 2.5 5 Q2.5 2.5 4 2 Z" fill="#e8f4fb"/></svg>+1 222 222 222</li>
      <li><svg class="contact-icon" viewBox="0 0 18 18"><rect x="5" y="1.5" width="8" height="5" fill="none" stroke="#e8f4fb" stroke-width="1.4"/><rect x="2" y="6.5" width="14" height="7" rx="1" fill="#e8f4fb"/><rect x="5" y="11.5" width="8" height="5" fill="#0e3a5c" stroke="#e8f4fb" stroke-width="1.4"/></svg>+1 333 333 333</li>
      <li class="link"><svg class="contact-icon" viewBox="0 0 18 18"><text x="9" y="14.5" text-anchor="middle" font-family="Open Sans, sans-serif" font-size="17" fill="#e8f4fb">@</text></svg>john.doe@brightpathwellness.com</li>
      <li class="link"><svg class="contact-icon" viewBox="0 0 18 18"><circle cx="9" cy="9" r="7.5" fill="none" stroke="#e8f4fb" stroke-width="1.4"/><ellipse cx="9" cy="9" rx="3.5" ry="7.5" fill="none" stroke="#e8f4fb" stroke-width="1.2"/><line x1="1.5" y1="9" x2="16.5" y2="9" stroke="#e8f4fb" stroke-width="1.2"/></svg>http://www.brightpathwellness.com/</li>
    </ul>
  </section>

</main>
</body>
</html>
```